This is a 20 X 30 Movie Poster for an Independent Film titled "Lantern"

Update - 8/8/2017
We are getting some very good designs but please keep in mind that our story has a primary focus on the relationship between two brothers - the football piece is there - but as a minor character. Also keep in mind our primary characters are African American - we have seen some cool designs but with white characters - lastly - we are seeking a true movie poster look - please check some samples on www.reelvaultlist.com - good luck and thanks for the efforts!

We need to have a MOVIE POSTER type visual. Our story originally began as one about Ray Kessick - Who was a player for the Fairhaven Otters UPL team and later committed suicide due to a brain disease known as CTE. I have included the winning poster from that campaign as a reference - As you can see the designer did a great job for us of incorporating the important concepts of our story - Kessick played for the Fairhaven Otters so Otters Field was used - He won UPL Player of the Year - The trophy was used - He owned a business - That photo was used - this designed worked for us!

HOWEVER - As the research for the story evolved we discovered a better story was that of Raymond's Brother Gordon - Our story will now focus on him!!!

Ray and Gordon had a typical relationship - Gordon was the older brother yet always lived in the shadows of Raymond - Raymond was an All-American Football player at Briarcliff State, played profession football for several years and then had a successful business career until the effects of CTE began to overtake him.

GORDON was the one behind the scenes - While Gordon also suffered a Traumatic Brian Injury - He was the one who was "the guy behind the scenes" through much of his brother success.

SOOOO We need something to capture this relationship - Open to any concepts.

The title of the film is "LANTERN"

While it might be to wordy to put on the poster our TAGLINE IS: "The incredible story of Gordon Ellis Kessick and his dramatic journey through a life impacted by concussions, traumatic brain injuries, and CTE -

The should be LARGE AND BOLD and if the design does include the tagline this should be much smaller.

Written By: Loretta J. Pask and Dennis K. Pask should be on the bottom of the poster.

While we do not need a poster with as much detail as the one you see with SALT AND IRON photo (We don't have great photos of Gordon to work with) we are open to not showing faces - Using silhouette or something like the poster for the film THE LONG ROW!

Again - WE HAVE NOTHING SOLID IN MIND - BE CREATIVE - We will come back to our winner for more designs once the films funding is released - So this could end up being a great contract for the person who captures our attention!

Our producers have made their selection for this contest. Thank you all for your efforts - There were several designs that were debated on over the course of the last two weeks. When we go into production with this project, we may be reaching out to several of you and assigning more funding to some of your submissions. Thank you all!

Target Market(s)

Football related with issues surrounding concussions but a Wren Family Film.

Industry/Entity Type

Movie

Other font styles liked:
• Designer's Choice

Colors

Designer to choose colors to be used in the design.

Requirements
Must have
• The title of the film is "LANTERN"
• Something that captures the relationship of two brothers - One who was always behind the scenes until his brother's suicide - The brother LANTERNS though a difficult life to bring to life a foundation to honor his fallen brother by being the world leader in concussion, traumatic brain injury and CTE education.
Nice to have
• Tagline: Somewhere - If it is not too wordy - Can be found in Project Description
• WREN FAMILY SEAL - Not too large

```html
<!DOCTYPE html>
<html lang="en">
<head>
<meta charset="utf-8">
<title>Lantern — Film Poster</title>
<link href="https://fonts.googleapis.com/css2?family=Inter:wght@400;700;800&display=swap" rel="stylesheet">
<style>
  :root {
    --stage: #141414;
    --paper: #dcdcdc;
    --ink: #111111;
    --rule: #3a3a3a;
    --helmet-dark: #161616;
    --helmet-mid: #4a4a4a;
  }
  * { margin: 0; padding: 0; box-sizing: border-box; }
  html, body {
    width: 1200px;
    height: 1000px;
    overflow: hidden;
    background: var(--stage);
    font-family: "Inter", "Helvetica Neue", Arial, sans-serif;
  }
  .poster {
    position: absolute;
    left: 335px;
    top: 102px;
    width: 531px;
    height: 797px;
    background: var(--paper);
    color: var(--ink);
  }
  .helmet-art {
    position: absolute;
    border-radius: 50% 46% 40% 44%;
    background: radial-gradient(ellipse at 40% 40%, var(--helmet-mid) 0%, var(--helmet-dark) 55%, var(--helmet-dark) 100%);
  }
  .helmet-art--upper { left: 127px; top: 28px; width: 298px; height: 275px; }
  .helmet-art--lower { left: 103px; top: 335px; width: 314px; height: 253px; }
  .title {
    position: absolute;
    right: 26px;
    top: 590px;
    font-weight: 800;
    font-size: 100px;
    line-height: 1;
    letter-spacing: -3px;
  }
  .credits-band {
    position: absolute;
    left: 0;
    right: 0;
    top: 715px;
    bottom: 0;
    border-top: 1px solid var(--rule);
    display: grid;
    grid-template-columns: 90px 132px 1fr;
  }
  .seal-cell {
    border-right: 1px solid var(--rule);
    display: flex;
    align-items: center;
    justify-content: center;
  }
  .seal-badge {
    width: 34px;
    height: 34px;
    border-radius: 8px;
    background: var(--ink);
  }
  .writers {
    padding: 26px 0 0 33px;
    font-weight: 700;
    font-size: 9.5px;
    line-height: 1.3;
  }
  .tagline {
    padding: 26px 40px 0 0;
    font-weight: 400;
    font-size: 9.2px;
    line-height: 1.3;
  }
</style>
</head>
<body>
  <main class="poster">
    <div class="helmet-art helmet-art--upper" role="img" aria-label="Black football helmet in halftone, sliced through and split apart, facing right"></div>
    <div class="helmet-art helmet-art--lower" role="img" aria-label="Second black football helmet in halftone, sliced near the back, facing right"></div>

    <h1 class="title">Lantern.</h1>

    <footer class="credits-band">
      <div class="seal-cell"><span class="seal-badge" aria-hidden="true"></span></div>
      <p class="writers">Written by<br>Loretta J. Pask<br>and Dennis K.</p>
      <p class="tagline">The incredible story of Gordon Ellis Kessick<br>and his dramatic journey through a life impacted by<br>concussions, traumatic brain injuries, and CTE.</p>
    </footer>
  </main>
</body>
</html>
```